Kettles - Eggs For Sale Sign

Would like a graphic quality image of a EGGS FOR SALE SIGN ... am getting a local outdoor sign company to print the sign and attach it to a frame.

this is going to be outside by the gate to our farm ... would like the sign to "POP" ... DRAW ATTENTION ... as it were ... please.

I think we need it about 36”(w) x 30”(h) ... maybe 48”x36” ... not sure ... need about an extra 1 1/2” border around also so that we can frame this into a wooden frame ...

The color picture is similar to the pattern we like ... the fonts you are welcome to just blow us out of the water with ... we are not tied down to any particular font ... like the “WANTED” posters of old ... sorta.

Logo Text

Bramble Nook Acres

Colors

Requirements
Must have
• Some type of Fire Fly art ... not to modern ... not too comic book ...
Nice to have
• phone number
• call or text

```html
<!DOCTYPE html>
<html lang="en">
<head>
<meta charset="utf-8">
<title>Bramble Nook Acres – Eggs For Sale</title>
<link rel="stylesheet" href="https://fonts.googleapis.com/css2?family=Fira+Sans:wght@700;800;900&display=swap">
<style>
  :root {
    --frame: #000000;
    --wood-dark: #7e3f1f;
    --wood-mid: #a45a2e;
    --wood-light: #b56a3a;
    --ink-white: #ffffff;
    --teal: #19c4bf;
    --glow: #f7c600;
    --silhouette: #0c0a08;
  }
  html, body {
    margin: 0;
    padding: 0;
    width: 1200px;
    height: 900px;
    overflow: hidden;
    background: var(--frame);
  }
  .sign {
    position: relative;
    width: 1200px;
    height: 900px;
    background: var(--frame);
    font-family: "Fira Sans", sans-serif;
  }
  .board {
    position: absolute;
    left: 34px;
    top: 34px;
    width: 1132px;
    height: 832px;
    background: linear-gradient(100deg, var(--wood-mid) 0%, var(--wood-dark) 30%, var(--wood-light) 55%, var(--wood-dark) 80%, var(--wood-mid) 100%);
  }
  .farm-name {
    position: absolute;
    left: 0;
    top: 70px;
    width: 1200px;
    height: 124px;
    margin: 0;
    display: flex;
    align-items: center;
    justify-content: center;
    gap: 22px;
    color: var(--ink-white);
    font-weight: 800;
    font-size: 80px;
    line-height: 1;
    letter-spacing: 1px;
    white-space: nowrap;
  }
  .farm-name__mark {
    flex: none;
    width: 104px;
    height: 104px;
    border-radius: 50%;
    background: var(--glow);
  }
  .tagline {
    position: absolute;
    left: 0;
    top: 226px;
    width: 1200px;
    margin: 0;
    text-align: center;
    color: var(--ink-white);
    font-weight: 800;
    font-size: 70px;
    line-height: 1;
  }
  .egg-badge {
    position: absolute;
    left: 0;
    top: 0;
    width: 1200px;
    height: 900px;
  }
  .egg-badge .arc-label {
    fill: var(--teal);
    font-family: "Fira Sans", sans-serif;
    font-weight: 800;
    font-size: 50px;
    letter-spacing: 6px;
  }
  .egg-badge .oval {
    fill: var(--ink-white);
    stroke: var(--teal);
    stroke-width: 9;
  }
  .egg-badge .product {
    fill: var(--teal);
    font-family: "Fira Sans", sans-serif;
    font-weight: 800;
    font-size: 136px;
  }
  .hen {
    position: absolute;
    top: 428px;
    width: 144px;
    height: 198px;
    background: var(--silhouette);
    border-radius: 50% 40% 45% 50% / 40% 35% 55% 60%;
  }
  .hen--left { left: 110px; }
  .hen--right { left: 948px; }
  .for-sale {
    position: absolute;
    left: 108px;
    top: 774px;
    margin: 0;
    color: var(--ink-white);
    font-weight: 800;
    font-size: 80px;
    line-height: 1;
  }
  .phone {
    position: absolute;
    right: 110px;
    top: 780px;
    margin: 0;
    color: var(--ink-white);
    font-weight: 800;
    font-size: 57px;
    line-height: 1;
  }
</style>
</head>
<body>
<main class="sign">
  <div class="board" role="img" aria-label="Background of weathered vertical brown barn-wood planks"></div>

  <h1 class="farm-name">
    <span>BRAMBLE NOOK</span>
    <span class="farm-name__mark" aria-hidden="true"></span>
    <span>ACRES</span>
  </h1>
  <p class="tagline">- fresh from the farm -</p>

  <svg class="egg-badge" viewBox="0 0 1200 900" aria-label="Organic free range eggs">
    <defs>
      <path id="arc-top" d="M 340 632 A 260 260 0 0 1 860 632"/>
      <path id="arc-bottom" d="M 330 458 A 270 270 0 0 0 870 458"/>
    </defs>
    <text class="arc-label"><textPath href="#arc-top" startOffset="50%" text-anchor="middle">ORGANIC</textPath></text>
    <ellipse class="oval" cx="600" cy="527" rx="249" ry="129"/>
    <text class="product" x="600" y="574" text-anchor="middle">EGGS</text>
    <text class="arc-label"><textPath href="#arc-bottom" startOffset="50%" text-anchor="middle">FREE RANGE</textPath></text>
  </svg>

  <div class="hen hen--left" role="img" aria-label="Black silhouette of a hen facing right"></div>
  <div class="hen hen--right" role="img" aria-label="Black silhouette of a hen facing left"></div>

  <p class="for-sale">FOR SALE</p>
  <p class="phone">(555) 014-2290</p>
</main>
</body>
</html>
```